Hello - we need a label design for our Quillon Health Hair Loss supplement. It is a natural hair loss supplement for black/african american women to regrow new hair and help restore hair loss & thinning hair due to vitamin deficiencies, traction alopecia, etc. It is a science based efficacious supplement with a centuries old medicinal herbal formula.
Attached is the logo & files of other generic competition and also Black hair products for your perusal. The label has to be a upscale and have an ethnic flair to it. The product is clinically effective, leveraged by Ancient Wisdom and Modern Science. The front of the label should include the following:
Quillon Health (logo)
Strand Renewal
Advanced Women’s Hair Loss Formula
TRACTION ALOPECIA THERAPY
- Prevents hair loss & restores thinning, fragile hair
- Promotes Natural Hair Growth
- Strengthens Hair for less breakage
- Visibly increases hair density & thickness
- Thicker, Stronger, Longer, Hydrated hair
- Promotes Follicle regeneration & Hair Growth
Site-Specific for hair loss & stunted growth
60 capsules 30-day supply
Target Market(s)
Black/African American Women
Look and feel

```html
<!DOCTYPE html>
<html lang="en">
<head>
<meta charset="utf-8">
<title>Quillon Health Strand Renewal – Label</title>
<link href="https://fonts.googleapis.com/css2?family=Montserrat:wght@700;800&family=Oswald:wght@500&family=Roboto+Condensed:wght@400;700&family=Roboto:wght@400;500&family=Russo+One&display=swap" rel="stylesheet">
<style>
  :root{
    --stage:#e6e6e6;
    --label-black:#101010;
    --band-grey:#232323;
    --gold:#c98a4b;
    --gold-light:#e4a86e;
    --gold-dark:#8f5427;
    --white:#ffffff;
    --text-soft:#e8e8e8;
    --bullet-grey:#9a9a9a;
  }
  *{margin:0;padding:0;box-sizing:border-box}
  html,body{width:1012px;height:1200px;overflow:hidden}
  body{background:var(--stage);position:relative;font-family:"Roboto Condensed",sans-serif}

  .label{
    position:absolute;left:16px;top:396px;width:980px;height:408px;overflow:hidden;
    background:radial-gradient(ellipse at 50% 40%,#1d1d1d 0%,var(--label-black) 70%);
    color:var(--white);
  }

  /* left panel */
  .claims{position:absolute;left:21px;top:26px;width:244px}
  .claim{display:flex;align-items:center;gap:8px;color:var(--gold);font-family:"Roboto",sans-serif;font-weight:500;font-size:10px;height:22.5px;border-bottom:1px solid var(--gold-dark)}
  .claim:last-child{border-bottom:none}
  .claim-bullet{width:6px;height:6px;background:var(--gold);flex:none}
  .story{position:absolute;left:21px;top:104px;width:244px;font-family:"Roboto",sans-serif;font-size:8.3px;line-height:11px;color:var(--text-soft)}
  .story p+p{margin-top:10px}
  .checks{position:absolute;left:21px;top:275px;width:250px;list-style:none;font-family:"Roboto",sans-serif;font-weight:500;font-size:8.6px;line-height:12px}
  .checks li{display:flex;gap:5px;margin-bottom:0.5px}
  .checks li::before{content:"✓";color:var(--gold);font-weight:700}

  /* centre panel */
  .brand{position:absolute;left:0;width:980px;top:62px;display:flex;justify-content:center;align-items:center;gap:7px}
  .brand-dot{width:12px;height:12px;border-radius:50%;background:var(--gold)}
  .brand-name{font-family:"Montserrat",sans-serif;font-weight:700;font-size:22px;color:var(--gold-light)}
  .product-name{position:absolute;left:0;width:980px;top:100px;text-align:center;font-family:"Montserrat",sans-serif;font-weight:800;font-size:44px;line-height:46px;letter-spacing:0.5px}
  .formula-banner{position:absolute;left:322px;top:197px;width:336px;height:37px;border-radius:7px;background:linear-gradient(180deg,var(--gold-light),var(--gold) 45%,var(--gold-dark));display:flex;align-items:center;justify-content:center;font-family:"Oswald",sans-serif;font-weight:500;font-size:17.5px;letter-spacing:1.2px;color:var(--label-black)}
  .therapy-title{position:absolute;left:322px;top:245px;font-family:"Roboto Condensed",sans-serif;font-weight:700;font-size:13.5px}
  .benefits{position:absolute;left:322px;top:264px;list-style:none;font-size:8.8px;line-height:12.6px;color:var(--text-soft)}
  .benefits li{display:flex;align-items:center;gap:6px}
  .benefit-bullet{width:4px;height:4px;border-radius:50%;background:var(--bullet-grey);flex:none}
  .portrait{position:absolute;left:590px;top:238px;width:122px;height:114px;background:radial-gradient(ellipse at 55% 45%,#6b4028 0%,#2a1a12 45%,var(--label-black) 80%)}

  /* supply band */
  .supply-band{position:absolute;left:0;top:352px;width:980px;height:56px}
  .supply-band svg{position:absolute;left:0;top:0}
  .count-box{position:absolute;left:322px;top:0;width:80px;height:48px;border:2px solid var(--gold);border-top:none;border-bottom:none;background:var(--band-grey);text-align:center;border-radius:8px 8px 0 0}
  .count-number{font-family:"Russo One",sans-serif;font-size:30px;line-height:34px;color:var(--white)}
  .count-unit{font-family:"Russo One",sans-serif;font-size:8px;color:var(--gold);letter-spacing:0.5px}
  .supply-text{position:absolute;left:411px;top:7px}
  .supply-days{font-family:"Roboto",sans-serif;font-weight:500;font-size:12.5px}
  .supply-sub{font-family:"Roboto",sans-serif;font-size:10.8px;margin-top:1px}

  /* right panel */
  .directions{position:absolute;left:718px;top:31px;width:240px;font-family:"Roboto",sans-serif;font-size:8.3px;line-height:11px;color:var(--text-soft)}
  .directions h3{color:var(--gold);font-size:8.3px;font-weight:500}
  .directions p+p{margin-top:11px}
  .disclaimer{position:absolute;left:719px;top:122px;width:240px;height:57px;border:1px solid var(--gold);padding:10px 13px;font-family:"Roboto",sans-serif;font-size:8.3px;line-height:11px}
  .maker{position:absolute;left:721px;top:200px;width:240px;height:83px;border:1px solid var(--gold);text-align:center}
  .maker-head{background:linear-gradient(180deg,var(--gold),var(--gold-dark));font-family:"Roboto",sans-serif;font-weight:500;font-size:9.5px;line-height:12px;padding:2px 0 3px}
  .maker-body{font-size:10.4px;line-height:13.5px;padding-top:4px}
  .ingredients{position:absolute;left:724px;top:300px;width:240px;font-family:"Roboto",sans-serif;font-size:8.3px;line-height:11px}
  .ingredients strong{color:var(--gold);font-weight:500}
</style>
</head>
<body>
<main class="label">
  <section class="claims">
    <div class="claim"><span class="claim-bullet"></span>Support Against Shedding and Thinning</div>
    <div class="claim"><span class="claim-bullet"></span>Care for Traction-Stressed Edges</div>
    <div class="claim"><span class="claim-bullet"></span>Targeted for Sparse Areas &amp; Slow Growth</div>
  </section>

  <section class="story">
    <p>Quillon Health regrowth blends deliver deep daily nourishment for thinning edges, breakage along the hairline, sparse and weakened strands, stress from tight styles, and low overall fullness.†</p>
    <p>Our Advanced Women’s Formula is crafted around the needs of women’s hair, pairing time-honored herbal traditions with current nutritional research to help you reach fuller, shinier, healthier hair. It blends standardized botanicals like He Shou Wu and Horse Chestnut Extract with key supporting nutrients such as Silica, Biotin and more, so QH’s Advanced Women’s Formula can help your hair reach its natural best, every day.†</p>
  </section>

  <ul class="checks">
    <li>Supports Fuller-Looking, Resilient-Feeling,<br>Healthier hair</li>
    <li>Natural, Vegan &amp; 100% Drug Free</li>
    <li>Research-Backed Ingredients</li>
    <li>Modern Science * Ancient Wisdom</li>
  </ul>

  <div class="brand"><span class="brand-dot"></span><span class="brand-name">Quillon Health</span></div>
  <h1 class="product-name">STRAND<br>RENEWAL</h1>
  <div class="formula-banner">ADVANCED WOMEN’S HAIR LOSS FORMULA</div>
  <h2 class="therapy-title">TRACTION ALOPECIA THERAPY</h2>
  <ul class="benefits">
    <li><span class="benefit-bullet"></span>Prevents hair loss &amp; restores thinning, fragile hair</li>
    <li><span class="benefit-bullet"></span>Promotes Natural Hair Growth</li>
    <li><span class="benefit-bullet"></span>Strengthens Hair for less breakage</li>
    <li><span class="benefit-bullet"></span>Visibly increases hair density &amp; thickness</li>
    <li><span class="benefit-bullet"></span>Thicker, Stronger, Longer, Hydrated hair</li>
    <li><span class="benefit-bullet"></span>Promotes Follicle regeneration &amp; Hair Growth</li>
  </ul>
  <div class="portrait" role="img" aria-label="Portrait photo of a woman with long, full, curly dark hair"></div>

  <section class="supply-band">
    <svg width="980" height="56" viewBox="0 0 980 56">
      <defs>
        <linearGradient id="gold-band" x1="0" y1="0" x2="0" y2="1">
          <stop offset="0" stop-color="#e4a86e"/><stop offset="0.5" stop-color="#c98a4b"/><stop offset="1" stop-color="#8f5427"/>
        </linearGradient>
      </defs>
      <rect x="0" y="0" width="980" height="56" fill="#232323"/>
      <path d="M0 48 H640 L660 31 H980 V56 H0 Z" fill="url(#gold-band)"/>
    </svg>
    <div class="count-box"><div class="count-number">60</div><div class="count-unit">CAPSULES</div></div>
    <div class="supply-text">
      <div class="supply-days">30-DAY SUPPLY</div>
      <div class="supply-sub">Site-Specific for hair loss &amp; stunted growth</div>
    </div>
  </section>

  <section class="directions">
    <h3>DIRECTIONS FOR USE:</h3>
    <p>Take 1 capsule twice a day with food. Do not exceed the suggested amount. Ideally taken once after waking and once before going to sleep.</p>
    <p>FOR BEST RESULTS, USE THIS PRODUCT DAILY FOR AT LEAST 3-4 MONTHS. INDIVIDUAL RESULTS MAY VARY.</p>
  </section>
  <div class="disclaimer">These statements have not been evaluated by the Food and Drug Administration. This product is not intended to diagnose, treat, cure, or prevent any disease</div>
  <div class="maker">
    <div class="maker-head">FORMULATED BY &amp; MANUFACTURED<br>EXCLUSIVELY FOR:</div>
    <div class="maker-body">Quillon Health,<br>Marlow Falls, Ct. 06100 * USA<br>support@ quillonvita.com</div>
  </div>
  <p class="ingredients"><strong>INGREDIENTS:</strong> Lorem Ipsum is simply dummy text of the printing and typesetting industry. Lorem Ipsum has been the industry's standard dummy text ever since the 1500s.</p>
</main>
</body>
</html>
```